Advertisement for tellmark Ad

We are looking to copy a mailer style design that would normally be sent out to a mailbox. However we have decided to simply use it and run an add on Tellmark. please check photo sizes for tellmark to make sure your design will work.

also please try to use the colors from our website: riverbendhollow@mailnest.com

we want the same layout as the ad we sent in the files, with different photos and color scheme.

Target Market(s)

dog owners with busy schedules

Font styles to use
Sans Serif

Colors

Designer to choose only greyscale colors for use in the design.

```html
<!DOCTYPE html>
<html lang="en">
<head>
<meta charset="utf-8">
<title>Riverbend Hollow – Not Your Typical Dog Daycare</title>
<link rel="stylesheet" href="https://fonts.googleapis.com/css2?family=Josefin+Sans:wght@400;600;700&family=Lato:wght@400&display=swap">
<style>
  :root {
    --panel: #9b9b9b;
    --panel-light: #b4b4b4;
    --panel-band: #cdcdcd;
    --white: #ffffff;
    --ink: #111111;
    --band-top: #474747;
    --band-bottom: #222222;
    --offer: #f2f2f2;
    --divider: #8a8a8a;
    --photo-light: #d2d2d2;
    --photo-mid: #8a8a8a;
    --photo-dark: #4a4a4a;
    --photo-subject: #6e6e6e;
  }
  * { margin: 0; padding: 0; box-sizing: border-box; }
  html, body { width: 1200px; height: 750px; overflow: hidden; background: #ffffff; }
  .ad {
    position: relative;
    width: 1200px;
    height: 750px;
    overflow: hidden;
    font-family: "Josefin Sans", sans-serif;
  }
  .dog-photo {
    position: absolute;
    left: 0; top: 0;
    width: 620px; height: 589px;
    background:
      radial-gradient(ellipse at 45% 55%, #a8a8a8 0%, var(--photo-subject) 30%, transparent 58%),
      linear-gradient(160deg, var(--photo-light) 0%, var(--photo-mid) 45%, var(--photo-dark) 100%);
  }
  .panel {
    position: absolute;
    left: 0; top: 0;
    width: 1200px; height: 589px;
  }
  .brand {
    position: absolute;
    left: 52px; top: 60px;
    display: flex;
    align-items: center;
    gap: 10px;
    font-weight: 700;
    font-size: 22px;
    letter-spacing: 1px;
    color: var(--ink);
  }
  .brand-dot {
    width: 16px; height: 16px;
    border-radius: 50%;
    background: var(--ink);
  }
  .headline {
    position: absolute;
    right: 61px; top: 128px;
    text-align: right;
    color: var(--white);
    font-weight: 700;
    font-size: 64px;
    line-height: 75px;
    white-space: nowrap;
  }
  .services {
    position: absolute;
    left: 610px; top: 290px;
    list-style: none;
    color: var(--ink);
    font-weight: 400;
    font-size: 30px;
    line-height: 40px;
    white-space: nowrap;
  }
  .services .aside { font-size: 23px; line-height: 26px; }
  .contact {
    position: absolute;
    right: 44px; top: 509px;
    text-align: right;
    font-family: "Lato", sans-serif;
    font-style: normal;
    font-size: 18px;
    line-height: 24.5px;
    color: var(--ink);
  }
  .offers {
    position: absolute;
    left: 0; top: 589px;
    width: 1200px; height: 161px;
    background: linear-gradient(180deg, var(--band-top), var(--band-bottom));
  }
  .offer {
    position: absolute;
    top: 38px;
    transform: translateX(-50%);
    text-align: center;
    color: var(--offer);
    font-weight: 700;
    font-size: 31px;
    line-height: 42px;
    white-space: nowrap;
  }
  .offer sup {
    font-size: 14px;
    line-height: 0;
    position: relative;
    top: -4px;
    vertical-align: top;
  }
  .offer-daycare { left: 216px; }
  .offer-bath { left: 600px; }
  .offer-groom { left: 1003px; }
  .divider {
    position: absolute;
    top: 35px;
    height: 92px;
    border-left: 2px dotted var(--divider);
  }
  .divider-1 { left: 438px; }
  .divider-2 { left: 800px; }
  .footnote {
    position: absolute;
    right: 24px; bottom: 8px;
    font-family: "Lato", sans-serif;
    font-size: 16px;
    color: var(--white);
  }
</style>
</head>
<body>
<main class="ad">
  <div class="dog-photo" role="img" aria-label="Black and white photo of a happy beagle trotting across a sunny grassy field"></div>

  <svg class="panel" viewBox="0 0 1200 589" aria-hidden="true">
    <polygon points="417,0 1200,0 1200,589 600,589" fill="var(--panel)"/>
    <polygon points="425,0 890,0 560,215" fill="var(--panel-light)" opacity="0.8"/>
    <polygon points="640,0 1050,0 760,140" fill="var(--panel-light)" opacity="0.45"/>
    <polygon points="1200,390 1070,462 1200,500" fill="var(--panel-light)" opacity="0.7"/>
    <polygon points="573,502 1200,502 1200,589 600,589" fill="var(--panel-band)"/>
  </svg>

  <div class="brand"><span class="brand-dot"></span>RIVERBEND HOLLOW</div>

  <h1 class="headline">NOT YOUR TYPICAL<br>DOG DAYCARE</h1>

  <ul class="services">
    <li>SAFE OPEN-PLAY DAYCARE</li>
    <li>EXERSISE &amp; EDUCATION</li>
    <li>FUN FILLED DAYS WITH THEIR BFFF</li>
    <li class="aside">(BEST&nbsp; FURRY FRIENDS FOREVER)</li>
  </ul>

  <address class="contact">
    Riverbend Hollow Canine Activity Centre<br>
    418 North Mill Road Maple Grove IA<br>
    555-214-0387
  </address>

  <section class="offers">
    <p class="offer offer-daycare">FREE FIRST<br>DAY OF DAY CARE<sup>*</sup></p>
    <span class="divider divider-1"></span>
    <p class="offer offer-bath">ONE FREE<br>BATH<sup>*</sup></p>
    <span class="divider divider-2"></span>
    <p class="offer offer-groom">$20 OFF<br>FIRST GROOM<sup>*</sup></p>
    <p class="footnote">*Advanced Reservation required Call to schedule your appoinment.</p>
  </section>
</main>
</body>
</html>
```